Independent Christian Artist needs a Cd Cover for an EP Release

We need a Cd Cover designed for a EP that will be a digital release.
Project Name: Carried by Dawn

Concept: Red Neon Heart with Black Background, We are open to design creativity. We want the heart to look creative, different. I am open to different textures with the heart and the background as long as it is tasteful

The design must meet these requirements
1400 x 1400 pixels minimum; 3000 x 3000 pixels maximum.
PNG, GIF, JPG, or JPEG file type.
150-300 dpi (300 dpi is the best)
Less than 25mb.
RGB color scheme (not CMYK)

Industry/Entity Type

Music Download

Font styles to use
Sans Serif

Colors
ec1f27
1b1b1b

Requirements
Must have
• Album Name “Carried by Dawn” Artists Name “Tom Farrow”
Should not have
• an anatomical heart, symbols or words other than the album name and artist name.

```html
<!DOCTYPE html>
<html lang="en">
<head>
<meta charset="utf-8">
<title>Carried by Dawn — Tom Farrow</title>
<link rel="stylesheet" href="https://fonts.googleapis.com/css2?family=Open+Sans:wght@400&display=swap">
<style>
  :root {
    --signal-red: #ec1f27;
    --deep-black: #000000;
    --type-white: #ffffff;
  }
  html, body {
    margin: 0;
    padding: 0;
    width: 1200px;
    height: 1200px;
    overflow: hidden;
    background: var(--signal-red);
  }
  .cover {
    display: block;
    width: 1200px;
    height: 1200px;
  }
  .cover__frame { fill: var(--signal-red); }
  .cover__field { fill: var(--deep-black); }
  .cover__heart { fill: var(--signal-red); }
  .cover__title {
    font-family: "Open Sans", sans-serif;
    font-weight: 400;
    font-size: 140px;
    fill: var(--type-white);
    text-anchor: middle;
  }
  .cover__artist {
    font-family: "Open Sans", sans-serif;
    font-weight: 400;
    font-size: 32px;
    letter-spacing: 27px;
    fill: var(--type-white);
    text-anchor: middle;
  }
</style>
</head>
<body>
<svg class="cover" viewBox="0 0 1400 1400" xmlns="http://www.w3.org/2000/svg" role="img" aria-label="Carried by Dawn by Tom Farrow">
  <rect class="cover__frame" x="0" y="0" width="1400" height="1400"/>
  <rect class="cover__field" x="118" y="118" width="1164" height="1164"/>
  <polygon class="cover__heart" points="
    410,232 575,232 575,313 658,313 658,396 742,396 742,313 825,313 825,232
    991,232 991,313 1074,313 1074,396 1157,396 1157,639 1074,639 1074,722
    991,722 991,805 908,805 908,888 825,888 825,970 742,970 742,1051
    658,1051 658,970 575,970 575,888 492,888 492,805 410,805 410,722
    327,722 327,639 244,639 244,396 327,396 327,313 410,313"/>
  <text class="cover__title" x="700" y="613">CARRIED BY</text>
  <text class="cover__title" x="700" y="732">DAWN</text>
  <text class="cover__artist" x="713" y="1163">TOM FARROW</text>
</svg>
</body>
</html>
```